Bref créative |
Harbourlea Dental Clinic | ||
business cards, letterhead and envelopes design | ||
Use same font as used in my logo | ||
Cutting-Edge Corporate Traditional Modern Professional Simple Bright & Fun-filled |
Dr. Kelsi Tomberg Ravinder | ||
Corrow Arcade - Shop 4.3C, 27 Fenwick Lane, Meadowbank, NSW 2114 |
kelsi@HarbourleaDentalClinic.com.au | ||
www.HarbourleaDentalClinic.com.au | ||
For Business Cards Please include: After-hours Emergency Service: Phone: 02 5173 6648 Mobile: 04 7825 1943 For Envelops Please include: Logo If not delivered please return to Corrow Arcade - Shop 4.3C, 27 Fenwick Lane, Meadowbank, NSW 2114 |
Appointment: For - Date - Time - If you are unable to keep your appointment, please contact us as soon as possible. |

```html
<!DOCTYPE html>
<html lang="en">
<head>
<meta charset="utf-8">
<title>Harbourlea Dental Clinic – Stationery</title>
<link href="https://fonts.googleapis.com/css2?family=Open+Sans:wght@400;600;700&display=swap" rel="stylesheet">
<style>
  :root{
    --board:#1f1f21;
    --board-light:#2b2b2e;
    --paper:#ffffff;
    --brand:#1b8fc9;
    --brand-dark:#0f5f95;
    --brand-light:#5fc1ea;
    --ink:#4a4f55;
    --ink-soft:#8b9096;
    --rule:#c9ccd0;
    --ghost:#eef1f3;
  }
  *{margin:0;padding:0;box-sizing:border-box}
  html,body{width:1200px;height:674px;overflow:hidden}
  body{
    font-family:"Open Sans",Arial,sans-serif;
    background:radial-gradient(ellipse at 50% 40%,var(--board-light),var(--board) 75%);
    position:relative;color:var(--ink);
  }
  .piece{position:absolute;background:var(--paper);overflow:hidden;box-shadow:0 2px 8px rgba(0,0,0,.45)}

  /* wordmark */
  .wordmark{display:flex;align-items:center;gap:4px;position:absolute}
  .wordmark__dot{width:11px;height:11px;border-radius:50%;background:var(--brand);flex:none}
  .wordmark__name{font-weight:700;color:var(--brand);font-size:8px;line-height:1.05;width:62px}

  .ghost-mark{position:absolute;border-radius:50%;background:var(--ghost)}

  .tiny{font-size:4.3px;line-height:1.45;color:var(--ink-soft)}
  .tiny strong{color:var(--ink);font-weight:600}

  /* letterhead */
  .letterhead{top:187px;width:324px;height:432px}
  .letterhead--plain{left:84px}
  .letterhead--memo{left:427px}
  .letterhead .wordmark{left:16px;top:14px}
  .letterhead__address{position:absolute;right:16px;top:14px;width:92px}
  .letterhead .ghost-mark{left:30px;bottom:36px;width:70px;height:70px}
  .swoosh{position:absolute;left:0;bottom:0;width:100%;height:60px}
  .footer-band{position:absolute;left:0;bottom:0;width:100%;height:13px;
    background:linear-gradient(90deg,var(--brand-dark),var(--brand),var(--brand-light));
    color:#fff;font-size:4.5px;text-align:center;line-height:13px}

  .memo-fields{position:absolute;left:32px;top:114px;width:260px;border-collapse:collapse;font-size:4px;color:var(--ink)}
  .memo-fields td{border:0.6px solid var(--rule);height:9px;padding:0 3px;width:25%}
  .memo-message{position:absolute;left:32px;top:170px;width:260px;height:128px;border:0.6px solid var(--rule);
    font-size:4px;padding:3px;font-weight:600}

  /* business cards */
  .card{height:65px}
  .card--name{left:775px;top:108px;width:396px;
    background:linear-gradient(90deg,#fff 0 44%,var(--brand-light) 58%,var(--brand-dark));}
  .card--name .wordmark{left:12px;top:24px}
  .card__name{position:absolute;right:12px;top:6px;color:#fff;font-size:9px;font-weight:700}
  .card__contact{position:absolute;right:12px;top:22px;width:140px;color:#e9f6fd}
  .card__contact.tiny{color:#e9f6fd}

  .card--detail{left:775px;top:182px;width:197px;
    background:linear-gradient(90deg,var(--brand-dark),var(--brand) 55%,#fff 55.5%)}
  .card--detail .card__person{position:absolute;left:8px;top:8px;width:95px;color:#fff}
  .card--detail .card__person .tiny{color:#e2f3fb}
  .card--detail .wordmark{right:6px;top:24px}
  .card--detail .wordmark__name{font-size:6px;width:46px}
  .card--detail .wordmark__dot{width:8px;height:8px}

  .card--appointment{left:977px;top:182px;width:194px;
    background:linear-gradient(90deg,#fff 72%,var(--brand-light) 72.5%,var(--brand-dark))}
  .card--appointment .card__body{position:absolute;left:8px;top:7px;width:130px}
  .appt-line{border-bottom:0.6px solid var(--rule);font-size:4.2px;color:var(--ink);height:7px;margin-bottom:2px}

  /* envelopes */
  .envelope--front{left:775px;top:283px;width:396px;height:228px}
  .envelope--front .wordmark{left:14px;top:14px}
  .envelope__return{position:absolute;left:14px;top:38px;width:120px}
  .envelope--front .ghost-mark{left:36px;bottom:10px;width:56px;height:56px}
  .envelope--front .footer-band{height:16px;line-height:16px}
  .envelope__web{position:absolute;left:0;bottom:22px;width:100%;text-align:center;font-size:4.5px;color:var(--ink-soft)}

  .envelope--back{left:775px;top:523px;width:396px;height:96px}
  .envelope__flap{position:absolute;left:0;top:0;width:100%;height:100%}
  .envelope--back .envelope__web{bottom:auto;top:30px;color:#fff;z-index:1}
</style>
</head>
<body>

<!-- letterhead -->
<section class="piece letterhead letterhead--plain">
  <div class="wordmark"><span class="wordmark__dot"></span><span class="wordmark__name">Harbourlea Dental Clinic</span></div>
  <div class="letterhead__address tiny">Corrow Arcade - Shop 4.3C, 27 Fenwick Lane, Meadowbank, NSW 2114<br>P: 02 5173 6648 · M: 04 7825 1943<br>kelsi@HarbourleaDentalClinic.com.au</div>
  <div class="ghost-mark"></div>
  <svg class="swoosh" viewBox="0 0 324 60" preserveAspectRatio="none">
    <path d="M0 40 Q160 22 324 44" fill="none" stroke="#cfe9f6" stroke-width="1"/>
    <path d="M0 46 Q170 30 324 50" fill="none" stroke="#e3f2fa" stroke-width="1"/>
  </svg>
  <div class="footer-band">www.HarbourleaDentalClinic.com.au</div>
</section>

<!-- memo letterhead -->
<section class="piece letterhead letterhead--memo">
  <div class="wordmark"><span class="wordmark__dot"></span><span class="wordmark__name">Harbourlea Dental Clinic</span></div>
  <div class="letterhead__address tiny">Corrow Arcade - Shop 4.3C, 27 Fenwick Lane, Meadowbank, NSW 2114<br>P: 02 5173 6648 · M: 04 7825 1943<br><strong>kelsi@HarbourleaDentalClinic.com.au</strong></div>
  <table class="memo-fields">
    <tr><td>TO:</td><td></td><td>DATE:</td><td></td></tr>
    <tr><td>COMPANY:</td><td></td><td>PAGES:</td><td></td></tr>
    <tr><td>PHONE:</td><td></td><td>FAX:</td><td></td></tr>
    <tr><td>EMAIL:</td><td></td><td>REF:</td><td></td></tr>
  </table>
  <div class="memo-message">MESSAGE:</div>
  <div class="ghost-mark"></div>
  <svg class="swoosh" viewBox="0 0 324 60" preserveAspectRatio="none">
    <path d="M0 40 Q160 22 324 44" fill="none" stroke="#cfe9f6" stroke-width="1"/>
    <path d="M0 46 Q170 30 324 50" fill="none" stroke="#e3f2fa" stroke-width="1"/>
  </svg>
  <div class="footer-band">www.HarbourleaDentalClinic.com.au</div>
</section>

<!-- business card front -->
<section class="piece card card--name">
  <div class="wordmark"><span class="wordmark__dot"></span><span class="wordmark__name">Harbourlea Dental Clinic</span></div>
  <div class="card__name">Dr. Kelsi Tomberg Ravinder</div>
  <div class="card__contact tiny">Phone: 02 5173 6648<br>Mobile: 04 7825 1943<br>kelsi@HarbourleaDentalClinic.com.au<br>www.HarbourleaDentalClinic.com.au</div>
</section>

<!-- business card detail -->
<section class="piece card card--detail">
  <div class="card__person">
    <div style="font-size:5.5px;font-weight:700">Kelsi Tomberg Ravinder</div>
    <div class="tiny">After-hours Emergency Service:<br>Phone: 02 5173 6648<br>Mobile: 04 7825 1943</div>
  </div>
  <div class="wordmark"><span class="wordmark__dot"></span><span class="wordmark__name">Harbourlea Dental Clinic</span></div>
</section>

<!-- appointment card -->
<section class="piece card card--appointment">
  <div class="card__body">
    <div style="font-size:5px;font-weight:700;color:var(--brand)">Appointment:</div>
    <div class="appt-line">For -</div>
    <div class="appt-line">Date - &nbsp;&nbsp;&nbsp;&nbsp;&nbsp;&nbsp;&nbsp;&nbsp;&nbsp;&nbsp; Time -</div>
    <div class="tiny" style="font-size:3.6px">If you are unable to keep your appointment, please contact us as soon as possible.</div>
  </div>
</section>

<!-- envelope front -->
<section class="piece envelope--front">
  <div class="wordmark"><span class="wordmark__dot"></span><span class="wordmark__name">Harbourlea Dental Clinic</span></div>
  <div class="envelope__return tiny">If not delivered please return to<br>Corrow Arcade - Shop 4.3C, 27 Fenwick Lane, Meadowbank, NSW 2114<br>P: 02 5173 6648</div>
  <div class="ghost-mark"></div>
  <div class="envelope__web">www.HarbourleaDentalClinic.com.au</div>
  <div class="footer-band"></div>
</section>

<!-- envelope back -->
<section class="piece envelope--back">
  <svg class="envelope__flap" viewBox="0 0 396 96" preserveAspectRatio="none">
    <defs>
      <linearGradient id="flapFill" x1="0" x2="1">
        <stop offset="0" stop-color="#0f5f95"/><stop offset=".5" stop-color="#1b8fc9"/><stop offset="1" stop-color="#5fc1ea"/>
      </linearGradient>
    </defs>
    <path d="M0 0 H396 V34 Q198 62 0 34 Z" fill="url(#flapFill)"/>
    <path d="M0 38 Q198 66 396 38" fill="none" stroke="#cfe9f6" stroke-width="1"/>
  </svg>
  <div class="envelope__web">www.HarbourleaDentalClinic.com.au</div>
</section>

</body>
</html>
```